Dry Cleaners Pick-up & Delivery Service

We are in the need of a post card design to hand out in public focused in our dry-cleaners pick up and delivery business services. The postcard must include a price list of most common items sent to the dry cleaners on a regular basis along with promotional sign-up deals and specials as advertised on our website. The color palette must match our website's color scheme - www.vorqualin.com - we would like to focus on our free pick-up and free delivery service. The hand out post card should look clean, organized and neat, yet modern in style projecting the cleanliness of the clothing articles that our customer let us take care of saving them time while we take care of this errand for them. All new customers receive a free high quality, heavy duty laundry bag with our business information and are encouraged to request for $10 of free dry cleaning on their first order, no strings attached, just for signing up to our service.We strive to please our customers and invest on them to have more free time on their hands, plain and simple. We also offer law enforcement uniform special, as the area we focus our routes is a high law enforcement residential community. The logo is attached and must be visible in the postcard as well as the website address and phone number 305-472-1946 as these are the main contact forms of clients reaching our business. This is home based business, we have a partnership with a dry cleaners business who does all of our route customers' dry cleaning needs. Our business is all about the marketing, sales and networking with corporate businesses. The postcard handout must have designs of both sides of the post card as well. They will not be used for mailing for the moment being, they will be only used to hand out.

Industry/Entity Type

Dry Cleaning

```html
<!DOCTYPE html>
<html lang="en">
<head>
<meta charset="utf-8">
<title>Vorqualin Postcard, Front and Back</title>
<link rel="stylesheet" href="https://fonts.googleapis.com/css2?family=Kalam:wght@400;700&family=Montserrat:wght@400;500;600&display=swap">
<style>
  :root {
    --page-bg: #e9eaec;
    --card-white: #ffffff;
    --panel-white: rgba(255, 255, 255, 0.9);
    --navy: #1f3f8f;
    --royal: #3558b0;
    --sky: #b9c9e6;
    --brand-green: #5a9e3c;
    --bag-green: #5cc247;
    --ink: #1b1b1b;
    --muted-ink: #333333;
  }
  * { box-sizing: border-box; margin: 0; padding: 0; }
  html, body {
    width: 1200px;
    height: 1000px;
    overflow: hidden;
    background: var(--page-bg);
  }
  .postcard {
    position: absolute;
    left: 240px;
    width: 720px;
    height: 470px;
    overflow: hidden;
    box-shadow: 0 5px 18px rgba(0, 0, 0, 0.18);
  }
  .postcard-front { top: 20px; background: var(--card-white); }
  .postcard-back { top: 510px; background: var(--sky); }

  /* shared brand block */
  .brand {
    position: absolute;
    left: 0;
    width: 100%;
    text-align: center;
  }
  .brand-name {
    display: inline-flex;
    align-items: center;
    gap: 8px;
    font-family: "Montserrat", sans-serif;
    font-weight: 500;
    color: var(--brand-green);
    letter-spacing: 0.5px;
  }
  .brand-dot {
    border-radius: 50%;
    background: var(--brand-green);
  }
  .brand-tagline {
    margin-top: 3px;
    font-family: "Montserrat", sans-serif;
    color: var(--muted-ink);
  }

  /* front */
  .garment-backdrop {
    position: absolute;
    inset: 0;
    background: linear-gradient(180deg, #fbfbfb 0%, #f1f2f4 22%, #c3d0e8 40%, #5f7fc2 62%, #2c4b9a 100%);
  }
  .band { position: absolute; left: 0; width: 100%; }
  .front-band-top { top: 140px; height: 19px; background: var(--royal); opacity: 0.85; }
  .front-band-middle { top: 322px; height: 18px; background: var(--navy); opacity: 0.8; }
  .front-band-bottom { top: 430px; height: 30px; background: var(--navy); opacity: 0.85; }

  .postcard-front .brand { top: 26px; }
  .postcard-front .brand-name { font-size: 32px; }
  .postcard-front .brand-dot { width: 12px; height: 12px; }
  .postcard-front .brand-tagline { font-size: 11px; }

  .panel { position: absolute; background: var(--panel-white); }
  .offer-panel {
    left: 34px; top: 175px; width: 412px; height: 130px;
    padding: 16px 18px 0 18px;
  }
  .offer-headline {
    font-family: "Kalam", cursive;
    font-weight: 700;
    font-size: 15px;
    line-height: 1.2;
    text-transform: uppercase;
    text-align: center;
    white-space: nowrap;
    color: var(--ink);
  }
  .offer-body {
    margin-top: 7px;
    font-family: "Montserrat", sans-serif;
    font-size: 9.5px;
    line-height: 1.4;
    color: var(--ink);
  }
  .phone-panel {
    left: 34px; top: 350px; width: 412px; height: 72px;
    display: flex; align-items: center; padding-left: 26px;
  }
  .phone-number {
    font-family: "Kalam", cursive;
    font-weight: 700;
    font-size: 33px;
    color: var(--ink);
    white-space: nowrap;
  }
  .pickup-panel {
    left: 466px; top: 175px; width: 220px; height: 247px;
    padding: 14px 14px 0 14px;
    text-align: center;
  }
  .laundry-bag-art {
    width: 80px; height: 72px; margin: 0 auto;
    border-radius: 20px 20px 12px 12px;
    background: linear-gradient(160deg, #7ad65e 0%, var(--bag-green) 55%, #3f9a30 100%);
  }
  .pickup-title {
    margin-top: 12px;
    font-family: "Kalam", cursive;
    font-weight: 700;
    font-size: 20px;
    color: var(--ink);
  }
  .pickup-body {
    margin-top: 4px;
    font-family: "Kalam", cursive;
    font-weight: 700;
    font-size: 10px;
    line-height: 1.3;
    text-transform: uppercase;
    color: var(--ink);
  }

  /* back */
  .postcard-back .brand { top: 18px; }
  .postcard-back .brand-name { font-size: 28px; }
  .postcard-back .brand-dot { width: 11px; height: 11px; }
  .postcard-back .brand-tagline { font-size: 10px; }

  .stripe { position: absolute; left: 0; width: 100%; height: 8px; background: var(--card-white); }
  .stripe-one { top: 100px; }
  .stripe-two { top: 206px; }
  .stripe-three { top: 308px; }

  .feature {
    position: absolute;
    left: 34px;
    width: 370px;
  }
  .feature-service { top: 118px; }
  .feature-special { top: 220px; }
  .feature-delivery { top: 322px; }
  .feature-title {
    font-family: "Kalam", cursive;
    font-weight: 700;
    font-size: 22px;
    line-height: 1.25;
    text-transform: uppercase;
    white-space: nowrap;
    color: var(--ink);
  }
  .feature-body {
    margin-top: 2px;
    font-family: "Montserrat", sans-serif;
    font-size: 10.5px;
    line-height: 1.4;
    color: var(--ink);
  }

  .price-panel {
    left: 430px; top: 120px; width: 256px; height: 262px;
    padding: 12px 18px 0 18px;
  }
  .price-title {
    font-family: "Kalam", cursive;
    font-weight: 700;
    font-size: 22px;
    text-align: center;
    color: var(--ink);
  }
  .price-list { list-style: none; margin-top: 6px; }
  .price-item {
    display: flex;
    justify-content: space-between;
    padding: 5px 0;
    border-bottom: 1px solid var(--sky);
    font-family: "Montserrat", sans-serif;
    font-size: 11.5px;
    color: var(--ink);
  }
  .price-item:last-child { border-bottom: none; }
  .price-amount { font-weight: 600; color: var(--navy); }

  .contact-band {
    position: absolute;
    left: 0; top: 400px; width: 100%; height: 70px;
    background: var(--navy);
    display: flex;
    align-items: center;
    justify-content: space-between;
    padding: 0 34px;
  }
  .contact-item {
    font-family: "Kalam", cursive;
    font-weight: 700;
    font-size: 24px;
    color: var(--card-white);
    white-space: nowrap;
  }
</style>
</head>
<body>
  <article class="postcard postcard-front">
    <div class="garment-backdrop" role="img" aria-label="Photo of freshly cleaned blue and white dress shirts hanging on wooden hangers"></div>
    <div class="band front-band-top"></div>
    <div class="band front-band-middle"></div>
    <div class="band front-band-bottom"></div>

    <header class="brand">
      <div class="brand-name"><span class="brand-dot"></span>Vorqualin</div>
      <div class="brand-tagline">Dry Cleaners Pick-up &amp; Delivery Services, LLC</div>
    </header>

    <section class="panel offer-panel">
      <h2 class="offer-headline">Call us and try the service for free and<br>get $10 off your first dry cleaning order.</h2>
      <p class="offer-body">Our delivery service is FREE of charge, even if it is a next-day service request, all you pay is for your dry cleaning or laundry service. No hidden delivery fees. Go ahead, try the service!</p>
    </section>

    <section class="panel phone-panel">
      <p class="phone-number">CALL 305-472-1946</p>
    </section>

    <section class="panel pickup-panel">
      <div class="laundry-bag-art" role="img" aria-label="Photo of a green drawstring laundry bag filled with clothes"></div>
      <h2 class="pickup-title">PICK-UP IS FREE!</h2>
      <p class="pickup-body">Fill it up. We will pick-up your free laundry bag (our free gift to you) at your home or office and deliver it back to you. No hidden or additional costs it's really that simple.</p>
    </section>
  </article>

  <article class="postcard postcard-back">
    <header class="brand">
      <div class="brand-name"><span class="brand-dot"></span>Vorqualin</div>
      <div class="brand-tagline">Dry Cleaners Pick-up &amp; Delivery Services, LLC</div>
    </header>

    <div class="stripe stripe-one"></div>
    <div class="stripe stripe-two"></div>
    <div class="stripe stripe-three"></div>

    <section class="feature feature-service">
      <h2 class="feature-title">Quality Service</h2>
      <p class="feature-body">We care for your items like they were our own. Your satisfaction is our top priority.</p>
    </section>

    <section class="feature feature-special">
      <h2 class="feature-title">Law Enforcement Special</h2>
      <p class="feature-body">Uniforms pressed and returned next day at a special route price for officers.</p>
    </section>

    <section class="feature feature-delivery">
      <h2 class="feature-title">Free Pick-up &amp; Delivery</h2>
      <p class="feature-body">No delivery fees, next-day service at no extra cost.</p>
    </section>

    <section class="panel price-panel">
      <h2 class="price-title">PRICE LIST</h2>
      <ul class="price-list">
        <li class="price-item"><span>Shirt (laundered)</span><span class="price-amount">$2.50</span></li>
        <li class="price-item"><span>Pants</span><span class="price-amount">$6.00</span></li>
        <li class="price-item"><span>Suit, 2 pieces</span><span class="price-amount">$12.00</span></li>
        <li class="price-item"><span>Dress</span><span class="price-amount">$10.00</span></li>
        <li class="price-item"><span>Jacket / Blazer</span><span class="price-amount">$7.00</span></li>
        <li class="price-item"><span>Uniform set</span><span class="price-amount">$8.00</span></li>
        <li class="price-item"><span>Sweater</span><span class="price-amount">$6.50</span></li>
      </ul>
    </section>

    <footer class="contact-band">
      <span class="contact-item">www.vorqualin.com</span>
      <span class="contact-item">CALL 305-472-1946</span>
    </footer>
  </article>
</body>
</html>
```